flyer design

Hey i want someone to design a flyer for my tree lopping company. The design must have these
Tree Removals
Pruning
Stump Grinding
Qualified Arborist
Shaping And Thinning
Weight Reduction
Palm Cleans and Removals
Fully Insured
Owner Operator
Pensioners Discount
Free Quotes

I want my logo and the photo with me standing in front of my truck the front side and then every other photo on the back

Please incorporate the colours in my logo to the design

It Company

```html
<!DOCTYPE html>
<html lang="en">
<head>
<meta charset="utf-8">
<title>Summit Tree Care – Flyer</title>
<link rel="stylesheet" href="https://fonts.googleapis.com/css2?family=Dosis:wght@400;500;600&family=Oswald:wght@500;600;700&display=swap">
<style>
  :root {
    --board: #3b3b3d;
    --navy: #27305a;
    --sky: #4fa9e0;
    --sky-light: #bfe0f5;
    --leaf: #6cc23a;
    --leaf-light: #c9ec9a;
    --paper: #ffffff;
    --ink: #1d1f2b;
    --frame: #3fb4e4;
    --list: #2b7fb8;
  }
  * { box-sizing: border-box; margin: 0; padding: 0; }
  html, body { width: 1200px; height: 852px; overflow: hidden; background: var(--board); }
  .board { position: relative; width: 1200px; height: 852px; background: var(--board); }

  .side-label {
    position: absolute; top: 38px; color: var(--paper);
    font: 600 30px/1 "Oswald", sans-serif; letter-spacing: 0.5px;
  }
  .side-label.back { left: 74px; }
  .side-label.front { left: 1048px; }

  .page { position: absolute; top: 98px; height: 684px; overflow: hidden; box-shadow: 0 2px 8px rgba(0,0,0,.5); }
  .page-back {
    left: 72px; width: 524px;
    background: linear-gradient(100deg, var(--sky) 0%, #7cc0ea 45%, #e9f4fb 75%, var(--paper) 100%);
  }
  .page-front {
    left: 618px; width: 526px;
    background:
      radial-gradient(ellipse 260px 700px at 30px 420px, var(--leaf) 0%, #8fd24f 45%, rgba(201,236,154,.6) 70%, rgba(255,255,255,0) 100%),
      linear-gradient(160deg, var(--leaf-light) 0%, var(--paper) 35%, var(--paper) 100%);
  }

  .photo { position: absolute; }
  .framed { border: 2px solid var(--paper); }
  .photo-frame { position: absolute; background: var(--paper); border: 2px solid var(--frame); }

  .disc {
    position: absolute; border-radius: 50%;
    background: radial-gradient(circle at 40% 35%, #ffffff 0%, #f1f3f5 60%, #d6dade 100%);
    box-shadow: 0 3px 8px rgba(0,0,0,.3);
  }
  .disc-photo { position: absolute; border-radius: 50%; }

  .brand-name {
    position: absolute; color: var(--navy); text-align: center;
    font-family: "Dosis", sans-serif; font-weight: 600; line-height: 1;
    letter-spacing: 1px;
  }

  .contact-lead {
    position: absolute; left: 22px; color: var(--navy);
    font: 400 18px/1 "Dosis", sans-serif;
  }
  .contact-phone { font: 700 22px/1 "Oswald", sans-serif; color: var(--navy); margin-left: 8px; }
  .contact-address {
    position: absolute; left: 22px; top: 662px; color: var(--ink);
    font: 500 9.5px/1 "Dosis", sans-serif;
  }

  .services-title {
    position: absolute; left: 126px; top: 228px; color: var(--navy);
    font: 500 31px/1 "Dosis", sans-serif; letter-spacing: 0.5px;
  }
  .service-list { position: absolute; list-style: none; }
  .service-list li {
    display: flex; align-items: center; gap: 6px; height: 23px;
    color: var(--list); font: 400 14.5px/1 "Dosis", sans-serif;
  }
  .service-list svg { flex: none; }

  .insured-badge {
    position: absolute; left: 18px; top: 358px; width: 92px; height: 92px;
    display: flex; align-items: center; justify-content: center; text-align: center;
    color: var(--ink); font: 700 19px/1.1 "Oswald", sans-serif;
  }

  .cta {
    position: absolute; left: 0; right: 0; top: 644px; text-align: center;
    color: var(--navy); font: 700 20px/1 "Oswald", sans-serif; letter-spacing: 0.8px;
  }
</style>
</head>
<body>
<div class="board">
  <div class="side-label back">BACK</div>
  <div class="side-label front">FRONT</div>

  <section class="page page-back">
    <div class="photo framed" style="left:25px;top:24px;width:152px;height:290px;background:linear-gradient(180deg,#9fb8d6,#dfe6ef 60%,#6d7466);" role="img" aria-label="Arborist climbing a tall bare trunk against a cloudy sky"></div>
    <div class="photo framed" style="left:186px;top:24px;width:152px;height:290px;background:linear-gradient(180deg,#2f6fd0,#5a8a52 55%,#7b7355);" role="img" aria-label="Tall gum tree under a blue sky"></div>
    <div class="photo framed" style="left:349px;top:24px;width:152px;height:290px;background:linear-gradient(180deg,#3d7fd6,#8aa2b8 50%,#8c6a55);" role="img" aria-label="Worker in an elevated platform trimming a tall palm beside a house"></div>

    <div class="photo-frame" style="left:23px;top:332px;width:324px;height:258px;">
      <div class="photo" style="left:4px;top:4px;width:141px;height:248px;background:linear-gradient(180deg,#d9e8f3,#7aa54a 35%,#6c6043 70%,#c9c6c0);" role="img" aria-label="Trimmed date palm in a backyard"></div>
      <div class="photo" style="left:150px;top:4px;width:166px;height:248px;background:linear-gradient(180deg,#4a8fd8,#5e8a3e 40%,#4a4a42 70%,#d8d8d4);" role="img" aria-label="Arborist cleaning a large palm in a yard"></div>
    </div>

    <div class="disc" style="left:372px;top:332px;width:120px;height:120px;"></div>
    <div class="disc-photo" style="left:380px;top:340px;width:104px;height:104px;background:radial-gradient(circle,#9a8a78 0%,#c47e3e 45%,#6fa047 80%);" role="img" aria-label="Stump grinder cutting into a tree stump"></div>

    <div class="disc" style="left:292px;top:462px;width:208px;height:208px;">
      <div class="brand-name" style="left:0;right:0;top:80px;font-size:26px;">SUMMIT<br>TREE CARE</div>
    </div>

    <p class="contact-lead" style="top:608px;">For More Information</p>
    <p class="contact-lead" style="top:632px;display:flex;align-items:baseline;">Please Contact <span class="contact-phone">000.000.0000</span></p>
    <p class="contact-address">Summit Tree Care, Suite 000, Cityname, Country Name.</p>
  </section>

  <section class="page page-front">
    <div class="disc" style="left:32px;top:34px;width:168px;height:168px;"></div>
    <div class="disc-photo" style="left:42px;top:44px;width:148px;height:148px;background:linear-gradient(180deg,#e3ebe2,#4f8a32 45%,#2f5e1e);" role="img" aria-label="Hands trimming a hedge with shears"></div>

    <div class="brand-name" style="left:256px;top:120px;width:244px;font-size:36px;">SUMMIT<br>TREE CARE</div>

    <h2 class="services-title">OUR SERVICES ARE...</h2>

    <ul class="service-list" style="left:128px;top:275px;">
      <li><svg width="13" height="13" viewBox="0 0 13 13"><rect x="1" y="2" width="10" height="10" fill="none" stroke="#2b3455" stroke-width="1.5"/><path d="M3 7l2.5 2.5L12 1.5" fill="none" stroke="#2b3455" stroke-width="1.8"/></svg>Tree Removals</li>
      <li><svg width="13" height="13" viewBox="0 0 13 13"><rect x="1" y="2" width="10" height="10" fill="none" stroke="#2b3455" stroke-width="1.5"/><path d="M3 7l2.5 2.5L12 1.5" fill="none" stroke="#2b3455" stroke-width="1.8"/></svg>Stump Grinding</li>
      <li><svg width="13" height="13" viewBox="0 0 13 13"><rect x="1" y="2" width="10" height="10" fill="none" stroke="#2b3455" stroke-width="1.5"/><path d="M3 7l2.5 2.5L12 1.5" fill="none" stroke="#2b3455" stroke-width="1.8"/></svg>Shaping And Thinning</li>
      <li><svg width="13" height="13" viewBox="0 0 13 13"><rect x="1" y="2" width="10" height="10" fill="none" stroke="#2b3455" stroke-width="1.5"/><path d="M3 7l2.5 2.5L12 1.5" fill="none" stroke="#2b3455" stroke-width="1.8"/></svg>Palm Cleans and Removals</li>
      <li><svg width="13" height="13" viewBox="0 0 13 13"><rect x="1" y="2" width="10" height="10" fill="none" stroke="#2b3455" stroke-width="1.5"/><path d="M3 7l2.5 2.5L12 1.5" fill="none" stroke="#2b3455" stroke-width="1.8"/></svg>Pensioners Discount</li>
    </ul>
    <ul class="service-list" style="left:349px;top:275px;">
      <li><svg width="13" height="13" viewBox="0 0 13 13"><rect x="1" y="2" width="10" height="10" fill="none" stroke="#2b3455" stroke-width="1.5"/><path d="M3 7l2.5 2.5L12 1.5" fill="none" stroke="#2b3455" stroke-width="1.8"/></svg>Pruning</li>
      <li><svg width="13" height="13" viewBox="0 0 13 13"><rect x="1" y="2" width="10" height="10" fill="none" stroke="#2b3455" stroke-width="1.5"/><path d="M3 7l2.5 2.5L12 1.5" fill="none" stroke="#2b3455" stroke-width="1.8"/></svg>Qualified Arborist</li>
      <li><svg width="13" height="13" viewBox="0 0 13 13"><rect x="1" y="2" width="10" height="10" fill="none" stroke="#2b3455" stroke-width="1.5"/><path d="M3 7l2.5 2.5L12 1.5" fill="none" stroke="#2b3455" stroke-width="1.8"/></svg>Weight Reduction</li>
      <li><svg width="13" height="13" viewBox="0 0 13 13"><rect x="1" y="2" width="10" height="10" fill="none" stroke="#2b3455" stroke-width="1.5"/><path d="M3 7l2.5 2.5L12 1.5" fill="none" stroke="#2b3455" stroke-width="1.8"/></svg>Owner Operator</li>
      <li><svg width="13" height="13" viewBox="0 0 13 13"><rect x="1" y="2" width="10" height="10" fill="none" stroke="#2b3455" stroke-width="1.5"/><path d="M3 7l2.5 2.5L12 1.5" fill="none" stroke="#2b3455" stroke-width="1.8"/></svg>Free Quotes</li>
    </ul>

    <div class="photo" style="left:68px;top:406px;width:424px;height:226px;border:2px solid var(--frame);background:linear-gradient(180deg,#8fb8e2 0%,#d8dde2 35%,#eef0ee 55%,#8a8c8e 80%,#6f7173 100%);" role="img" aria-label="Owner standing in front of his branded work truck and ute"></div>

    <div class="disc insured-badge">FULLY<br>INSURED</div>

    <p class="cta">PLEASE CONTACT US FOR FREE QUOTES</p>
  </section>
</div>
</body>
</html>
```